Flyer für Kassensysteme
Zielgruppe
Kassensysteme - für diesen Flyer ist die Zielgruppe - Vereine - Unternehmen welche Vereinsfeste / Straßenfeste / Karnevalsitzungen oder Hausmessen bz. Messeverkäufe durchführen
Aufgabenstellung
optimal wäre DIN A5 einseitig welches auch so als Werbemail versendet werden kann. (unsere Internetpräsenz soll für diesen Firmenzweig von uns dann identisch angepasst werden) also ein schnell zu erfassender Flyer das es um Leih und Mietkassen für oben genannte Aktivitäten geht. kleiner Preis große Ersparnis Transparenz einfach zu bedienen

```html
<!DOCTYPE html>
<html lang="de">
<head>
<meta charset="utf-8">
<title>Leih- / Mietkassen – Norvalo</title>
<link rel="stylesheet" href="https://fonts.googleapis.com/css2?family=Montserrat:wght@400;500;600;700;800&display=swap">
<style>
  :root {
    --stage: #bdbdbd;
    --paper: #ffffff;
    --hero-dark: #3d5a7c;
    --hero-mid: #6f93b8;
    --strip: #b3d2e8;
    --ink: #3a3a3a;
    --body: #4a4a4a;
    --brand: #3f5270;
    --divider: #a9cbe6;
    --accent: #6d2a6e;
    --footer: #4a4a4a;
    --phone: #a6c9e6;
    --white: #ffffff;
  }
  * { margin: 0; padding: 0; box-sizing: border-box; }
  html, body { width: 1200px; height: 1200px; overflow: hidden; }
  body {
    background: var(--stage);
    font-family: "Montserrat", sans-serif;
    position: relative;
  }
  .flyer {
    position: absolute;
    left: 191px; top: 20px;
    width: 818px; height: 1160px;
    background: var(--paper);
    overflow: hidden;
  }
  .hero {
    position: absolute; left: 0; top: 0; width: 100%; height: 410px;
    background: linear-gradient(180deg, var(--hero-dark) 0%, var(--hero-mid) 55%, #7fa2c4 100%);
  }
  .hero-strip {
    position: absolute; left: 0; top: 410px; width: 100%; height: 14px;
    background: var(--strip);
  }
  .title {
    position: absolute; left: 0; top: 48px; width: 100%;
    text-align: center; color: var(--white);
    font-size: 55px; font-weight: 800; letter-spacing: 0.5px;
  }
  .subtitle {
    position: absolute; left: 0; top: 110px; width: 100%;
    text-align: center; color: var(--white);
    font-size: 22px; font-weight: 700; line-height: 32px;
  }
  .product {
    position: absolute; left: 61px; top: 196px; width: 690px; height: 396px;
    border-radius: 18px;
    background: radial-gradient(ellipse at 60% 45%, #8a8f96 0%, #55595f 55%, rgba(60,63,68,0.85) 100%);
  }
  .brand {
    position: absolute; left: 55px; top: 655px; width: 220px;
    display: flex; align-items: center; gap: 14px;
  }
  .brand-dot { width: 40px; height: 40px; border-radius: 50%; background: var(--brand); flex: none; }
  .brand-name {
    color: var(--brand); font-weight: 700; font-size: 30px; letter-spacing: 1px;
  }
  .divider {
    position: absolute; left: 297px; top: 631px; width: 3px; height: 100px;
    background: var(--divider);
  }
  .lead {
    position: absolute; left: 321px; top: 638px; width: 450px;
    color: var(--ink); font-size: 15.5px; font-weight: 700; line-height: 22.4px;
  }
  .body-copy {
    position: absolute; left: 51px; top: 760px; width: 716px;
    color: var(--body); font-size: 15px; font-weight: 500; line-height: 22.4px;
  }
  .body-copy .line { display: block; text-align: justify; text-align-last: justify; white-space: nowrap; }
  .body-copy .line.last { text-align-last: left; }
  .cta {
    position: absolute; left: 110px; top: 924px; width: 598px; height: 45px;
    background: var(--accent); border-radius: 8px;
    color: var(--white); font-size: 15px; font-weight: 700;
    display: flex; align-items: center; justify-content: center;
  }
  .footer {
    position: absolute; left: 0; top: 1000px; width: 100%; height: 160px;
    background: var(--footer);
  }
  .contact-row {
    position: absolute; left: 0; top: 22px; width: 100%;
    display: flex; align-items: center; justify-content: center; gap: 24px;
  }
  .more-info { color: var(--white); font-size: 33px; font-weight: 700; }
  .phone-icon { width: 52px; height: 52px; }
  .phone-number { color: var(--phone); font-size: 34px; font-weight: 700; }
  .web {
    position: absolute; left: 0; top: 94px; width: 100%;
    text-align: center; color: var(--phone); font-size: 16.5px; font-weight: 700;
  }
</style>
</head>
<body>
  <article class="flyer">
    <div class="hero" role="img" aria-label="Foto eines Festes mit Gästen und Grillwürstchen, blau eingefärbt"></div>
    <div class="hero-strip"></div>
    <h1 class="title">LEIH- / MIETKASSEN</h1>
    <p class="subtitle">Sie planen bzw. veranstalten ein Vereinsfest eine<br>Hausmesse oder einen Sonderverkauf?</p>
    <div class="product" role="img" aria-label="Produktfoto: Kassensystem mit Touch-Display und Tastatur sowie Bondrucker"></div>

    <div class="brand">
      <span class="brand-dot"></span>
      <span class="brand-name">Norvalo</span>
    </div>
    <div class="divider"></div>
    <p class="lead">Sparen Sie Zeit und Nerven mit der transparenten Abrechnung über eine unserer Mietkassen - kinderleicht zu bedienen und mit allen Funktionen eines modernen Kassensystems ausgestattet.</p>

    <p class="body-copy">
      <span class="line">Unsere Mietkassen sind mit einem großen LCD-Display ausgesprochen</span>
      <span class="line">benutzerfreundlich. Auch Aushilfen ohne jegliche Vorkenntnisse können an dem</span>
      <span class="line">innovativen Kassensystem von Kassanova schnell und fehlerfrei bedienen. Mit großer</span>
      <span class="line">Tastatur für bis zu 75 verschiedene Artikel garantiert Ihnen eine hohe Flexibilität und</span>
      <span class="line">Transparenz gewährleistet. Das alles zu einem äußerst attraktiven, budgetfreundlichen</span>
      <span class="line last">Preis.</span>
    </p>

    <div class="cta">Für Vereine bieten wir unsere Leihkassen mit einer Miet-TSE an.</div>

    <footer class="footer">
      <div class="contact-row">
        <span class="more-info">MORE INFO</span>
        <svg class="phone-icon" viewBox="0 0 52 52" aria-hidden="true">
          <circle cx="26" cy="26" r="24" fill="none" stroke="var(--phone)" stroke-width="3"/>
          <path d="M18 14c1.5-1 3-1 4 .5l2.5 4c.8 1.3.5 2.6-.6 3.4l-1.6 1.2c1 2.6 3.2 4.8 5.8 5.8l1.2-1.6c.8-1.1 2.1-1.4 3.4-.6l4 2.5c1.5 1 1.5 2.5.5 4l-1.5 2c-1.3 1.6-3.5 2-5.5 1.2C22.5 35.5 16.5 29.5 14.2 22c-.8-2-.4-4.2 1.2-5.5z" fill="var(--phone)"/>
        </svg>
        <span class="phone-number">[0721] 55210-0</span>
      </div>
      <p class="web">https://www.norvalo-kassen.de/leih-mietkassen/</p>
    </footer>
  </article>
</body>
</html>
```